Salt Moon, Tin Heart

Hey Guys
Please visit our Chatterleaf page for the film. See what ideas you bring to the table for the movie poster.
Looking for creative and something fresh.
Check out cast on QVTK
Will use the stills from the film for actual poster and quality.
Thanks a million for taking an interest in our film. xoxo
Target Market(s)
2-50 year old, date night, girls night out
Industry/Entity Type
Movie

```html
<!DOCTYPE html>
<html lang="en">
<head>
<meta charset="utf-8">
<title>Salt Moon, Tin Heart — Poster</title>
<link rel="stylesheet" href="https://fonts.googleapis.com/css2?family=Oswald:wght@300;400&family=Inter:wght@300;800&display=swap">
<style>
  :root {
    --stage: #0b0b0b;
    --magenta: #d41ef2;
    --violet: #a23ff2;
    --indigo: #6f5ff0;
    --sky: #1aa4ee;
    --credit: #2a9be6;
    --paper: #eef3f1;
  }
  * { box-sizing: border-box; margin: 0; padding: 0; }
  html, body {
    width: 1200px; height: 1200px; overflow: hidden;
    background: var(--stage);
  }
  .poster {
    position: absolute; left: 240px; top: 42px;
    width: 719px; height: 1110px;
    background: var(--paper);
    overflow: hidden;
  }
  .still {
    position: absolute; inset: 0;
    background:
      radial-gradient(ellipse 38% 22% at 52% 24%, rgba(140,70,150,.75), rgba(140,70,150,0) 70%),
      radial-gradient(ellipse 30% 30% at 80% 50%, rgba(235,190,175,.9), rgba(235,190,175,0) 72%),
      radial-gradient(ellipse 34% 30% at 42% 62%, rgba(240,200,190,.9), rgba(240,200,190,0) 72%),
      radial-gradient(ellipse 20% 28% at 8% 55%, rgba(235,205,150,.6), rgba(235,205,150,0) 75%),
      radial-gradient(ellipse 40% 25% at 15% 85%, rgba(170,215,235,.7), rgba(170,215,235,0) 75%),
      radial-gradient(ellipse 30% 20% at 90% 12%, rgba(185,225,235,.8), rgba(185,225,235,0) 75%),
      linear-gradient(180deg, #eaf3ec 0%, #e6e6f0 45%, #edf1f0 100%);
  }
  .cast {
    position: absolute; top: 24px; left: 27px; right: 27px;
    display: flex; justify-content: space-between;
    font-family: "Oswald", sans-serif; font-weight: 400;
    font-size: 28px; letter-spacing: .3px; line-height: 1;
  }
  .cast span:nth-child(1) { color: var(--magenta); }
  .cast span:nth-child(2) { color: var(--violet); }
  .cast span:nth-child(3) { color: var(--indigo); }
  .cast span:nth-child(4) { color: var(--sky); }
  .title {
    position: absolute; right: 33px; top: 628px;
    display: flex; flex-direction: column; align-items: flex-start;
    font-family: "Inter", sans-serif; font-size: 92px;
    line-height: 84px; letter-spacing: -2px;
  }
  .title span {
    background: linear-gradient(90deg, var(--magenta), var(--sky));
    -webkit-background-clip: text; background-clip: text;
    color: transparent;
  }
  .title .light { font-weight: 300; }
  .title .bold { font-weight: 800; }
  .title .solid { background: none; color: var(--magenta); }
  .credits {
    position: absolute; left: 20px; right: 20px; top: 1006px;
    font-family: "Oswald", sans-serif; font-weight: 300;
    color: var(--credit); font-size: 12.5px; line-height: 23px;
    text-align: center; white-space: nowrap; letter-spacing: -.3px;
  }
  .lbl {
    display: inline-flex; flex-direction: column; vertical-align: middle;
    font-size: 4.5px; line-height: 5px; text-align: right; margin: 0 2px 0 4px;
  }
  .sm { font-size: 6px; }
</style>
</head>
<body>
  <main class="poster">
    <div class="still" role="img" aria-label="Film still: a couple leaning together forehead to forehead in soft pastel light with bokeh"></div>
    <header class="cast">
      <span>RAFE DUNMORE</span>
      <span>LINA CASTELL</span>
      <span>ORIEL HATCH</span>
      <span>BRAM TOLLIVER</span>
    </header>
    <h1 class="title">
      <span class="light">SALT</span>
      <span class="bold">MOON</span>
      <span class="light">TIN</span>
      <span class="bold solid">HEART</span>
    </h1>
    <footer class="credits">
      <p>DRIFTLIGHT PICTURES <span class="sm">PRESENTS A</span> PRODUCERS <span class="sm">A FILM BY</span> MARLA QUESTOV, TOBIN ASHVALE REYES &nbsp;LINA CASTELL &nbsp;RAFE DUNMORE “SALT MOON, TIN HEART”</p>
      <p><span class="lbl"><span>MUSIC</span><span>BY</span></span>NICO VALDARRE <span class="lbl"><span>COSTUME</span><span>DESIGNER</span></span>DESIGNER NAME <span class="lbl"><span>EDITED</span><span>BY</span></span>EDITORS NAME <span class="lbl"><span>PRODUCTION</span><span>DESIGNER</span></span>SABINE CORVO <span class="lbl"><span>DIRECTOR OF</span><span>PHOTOGRAPHY</span></span>ELLIS FENN HARU MINASE</p>
      <p><span class="lbl"><span>EXECUTIVE</span><span>PRODUCER</span></span>EX PRODUCER <span class="lbl"><span>PRODUCED</span><span>BY</span></span>PRODUCER ONE PRODUCER 2 <span class="lbl"><span>STORY</span><span>BY</span></span>MARLA QUESTOV</p>
      <p><span class="lbl"><span>SCREENPLAY</span><span>BY</span></span>MARLA QUESTOV DEAN HARLOW <span class="lbl"><span>DIRECTED</span><span>BY</span></span>MARLA QUESTOV, TOBIN ASHVALE REYES</p>
    </footer>
  </main>
</body>
</html>
```